New business card and project proposal template, letterhead

Hello, I'm looking for a new business card and project proposal template to go with my new logo. project Proposals are sent to clients as a pdf document. my updated website is www.brightharborfilms.com. Looking for a look of a hollywood studio. Not a lot of dark colors , Red can be used as am acent, but not as a main. (see logo)

Target Market(s)

Communication departments, marketing managers.

Industry/Entity Type

Videography

Colors
ec1f27

Requirements
Must have
• logo,
• Brightharbor Films Inc.
• #300 - 812 East Kingsway
• Vancouver BC V6K 2M8
• www.brightharborfilms.com
• morwen@brightharborfilms.com
• Direct: 604 291 4073
• vimeo.com/brightharborfilms
• twitter: @brightharbor
Should not have
• clowns

```html
<!DOCTYPE html>
<html lang="en">
<head>
<meta charset="utf-8">
<title>Brightharbor Films – Business Card</title>
<link rel="stylesheet" href="https://fonts.googleapis.com/css2?family=Montserrat:wght@700&family=Roboto:wght@400&display=swap">
<style>
  :root {
    --backdrop: #a8a6a7;
    --card: #f7f7f7;
    --ink: #231f20;
    --ink-soft: #4a4a4a;
    --accent: #8b1d2c;
    --band: #2b2626;
  }
  * { box-sizing: border-box; margin: 0; padding: 0; }
  html, body { width: 1200px; height: 1200px; overflow: hidden; }
  body { background: var(--backdrop); position: relative; font-family: "Roboto", Arial, sans-serif; color: var(--ink); }

  .card { position: absolute; background: var(--card); border-radius: 28px; overflow: hidden; }
  .card--front { left: 238px; top: 119px; width: 712px; height: 418px; }
  .card--back  { left: 231px; top: 644px; width: 711px; height: 417px; }

  .wordmark {
    position: absolute; font-family: "Montserrat", Arial, sans-serif; font-weight: 700;
    font-size: 46px; line-height: 1; color: var(--ink); white-space: nowrap; letter-spacing: 0.8px;
  }
  .tagline {
    position: absolute; font-size: 21px; line-height: 1; color: var(--ink-soft); white-space: nowrap; text-align: right;
  }
  .card--front .wordmark { left: 64px; top: 174px; width: 582px; text-align: center; }
  .card--front .tagline  { right: 64px; top: 221px; }

  .side-band { position: absolute; left: 0; top: 0; width: 60px; height: 100%; background: var(--band); }
  .side-rule { position: absolute; left: 60px; top: 0; width: 7px; height: 100%; background: var(--accent); }

  .card--back .wordmark { left: 98px; top: 47px; width: 584px; text-align: center; }
  .card--back .tagline  { right: 27px; top: 95px; }

  .person { position: absolute; left: 102px; top: 213px; }
  .person__name { font-family: "Montserrat", Arial, sans-serif; font-weight: 700; font-size: 24px; letter-spacing: 1px; line-height: 1; }
  .person__role { font-size: 16px; color: var(--ink-soft); margin-top: 8px; }

  .contact { position: absolute; list-style: none; font-size: 17px; line-height: 24px; }
  .contact li { display: flex; align-items: center; gap: 12px; white-space: nowrap; }
  .contact svg { width: 16px; height: 16px; flex: none; fill: var(--accent); }
  .contact--main { left: 102px; top: 292px; }
  .contact--social { left: 518px; top: 292px; }
  .contact--social li { gap: 10px; }
  .address { position: absolute; left: 102px; top: 372px; font-size: 17px; white-space: nowrap; }
</style>
</head>
<body>

  <section class="card card--front" aria-label="Card front">
    <div class="wordmark">BRIGHTHARBOR FILMS</div>
    <div class="tagline">telling stories. moving people.</div>
  </section>

  <section class="card card--back" aria-label="Card back">
    <div class="side-band"></div>
    <div class="side-rule"></div>

    <div class="wordmark">BRIGHTHARBOR FILMS</div>
    <div class="tagline">telling stories. moving people.</div>

    <div class="person">
      <div class="person__name">MORWEN</div>
      <div class="person__role">Managing Director</div>
    </div>

    <ul class="contact contact--main">
      <li>
        <svg viewBox="0 0 16 16" aria-hidden="true"><path d="M1 5c0-2 3-3 7-3s7 1 7 3v1h-4V4.5H5V6H1z"/><path d="M3 7h10l1 7H2z"/></svg>
        604 291 4073
      </li>
      <li>
        <svg viewBox="0 0 16 16" aria-hidden="true"><circle cx="8" cy="8" r="6.5" fill="none" stroke="currentColor" stroke-width="1.4" style="color:var(--accent)"/><path d="M1.5 7.3h13v1.4h-13z"/><path d="M7.3 1.5h1.4v13H7.3z"/></svg>
        www.brightharborfilms.com
      </li>
      <li>
        <svg viewBox="0 0 16 16" aria-hidden="true"><path d="M1 3h14v10H1zm1.6 1.3L8 8.6l5.4-4.3zM2.3 12h11.4V5.6L8 10 2.3 5.6z"/></svg>
        morwen@brightharborfilms.com
      </li>
    </ul>

    <ul class="contact contact--social">
      <li>
        <svg viewBox="0 0 16 16" aria-hidden="true"><circle cx="8" cy="8" r="6"/></svg>
        /brightharborfilms
      </li>
      <li>
        <svg viewBox="0 0 16 16" aria-hidden="true"><circle cx="8" cy="8" r="6"/></svg>
        @brightharbor
      </li>
    </ul>

    <div class="address">#300 - 812 East Kingsway Vancouver BC V6K 2M8</div>
  </section>

</body>
</html>
```